Medical Education and Learning Portal refresh

We at uVeldra Limited have developed a learning platform for medical students. It is based around multiple choice questions, but has social and gaming elements built in to make it fun. It will be used on desktop and mobile devices.

I am looking for a refresh of the 'dated' design into something modern and transferrable between devices.

Note that I have a 'focus group' of Medical Students on 4 February where the Top 3-4 designs will be shown to them for them to pick the winner.

I have also uploaded screenshots of the current site. Essentially I would like to reduce the complexity of design into 2-3 pages (currently unlogged in front/home page, logged in page with options, answer questions page, competition page, revision page/summary pages etc). What I am really after is a good clean colour scheme & structure.

If we get the design colour scheme right then I can pay additionally for coding and maybe some additional structure to pages.
Updates

Target Market(s)

Healthcare/Medical Students

Industry/Entity Type

Healthcare

Number of Pages Required

4 page

Font styles to use
Serif
Sans Serif

Requirements
Must have
• 'Clean' Web 2.0 (or later) feel to it.
• I also expect that the images for the trophies are 'cleaned up (each trophy has a bronze/silver/platinum version as users increase their score. I am looking for these to be clean and simple but fun!
• I also need the final design to be transferrable from a desktop browser to a mobile device. I will need designs for home page/content page/Q&A page.
• I previously had a side panel float over the site but that is dated now and I would like to have a page with each element clearly on it and any information would briefly float over this but not take the focus away from the main function of the page.
• I have included the 'bronze', 'silver', 'gold' trophy icons in the files. These are fine in one sense but ideally the colours will blend well too ...
• The following article summarises my must haves:
• http://pagecraftnotes.example/web-design/web-2-0-design-style-guide/
Nice to have
• Creative concept for presenting MCQ's to students, with a timer and box of information about the question (level of the question, the percent of student who get it right ... etc).
Should not have
• Too much complexity ... clean with a few colours is what I am after
• Note too that my logo is not changing and the colours should blend with this.

```html
<!DOCTYPE html>
<html lang="en">
<head>
<meta charset="utf-8">
<title>uVeldra – The Medical Peer Review</title>
<link rel="stylesheet" href="https://fonts.googleapis.com/css2?family=Lato:wght@400;700;900&display=swap">
<style>
:root{
  --teal:#3dc1c1;
  --teal-soft:#5fcdcc;
  --navy:#3f6590;
  --steel:#4a6f96;
  --steel-dark:#375a80;
  --orange:#fd9b00;
  --ink:#222;
  --white:#fff;
  --rule:#c9cfd6;
}
*{box-sizing:border-box;margin:0;padding:0}
html,body{width:1200px;height:2667px;overflow:hidden}
body{font-family:'Lato',Arial,sans-serif;color:var(--ink);background:var(--white);position:relative}
.abs{position:absolute}
a{color:inherit;text-decoration:none}

/* header */
.site-header{left:0;top:0;width:1200px;height:76px;background:var(--white)}
.brand{left:71px;top:6px}
.brand-name{font-size:40px;font-weight:700;color:var(--steel);line-height:44px;letter-spacing:.5px}
.brand-tag{font-size:11px;font-weight:700;color:var(--ink);margin-left:2px}
.social-dot{width:36px;height:36px;border-radius:50%}
.btn{display:flex;align-items:center;justify-content:center;color:var(--white);font-size:16px}
.btn-orange{background:var(--orange)}
.btn-steel{background:var(--steel)}

/* nav */
.main-nav{left:0;top:76px;width:1200px;height:48px;background:var(--steel);display:flex;padding-left:72px}
.nav-item{display:flex;flex-direction:column;align-items:center;justify-content:flex-end;padding:0 10px 5px;color:var(--white);font-size:14.5px;border-right:1px solid rgba(255,255,255,.2);position:relative}
.nav-item:last-child{border-right:none}
.nav-item::before{content:"";width:10px;height:9px;background:var(--white);border-radius:2px;margin-bottom:5px;opacity:.95}
.nav-item.is-active{text-decoration:underline}

/* hero */
.hero{left:0;top:124px;width:1200px;height:552px;background:var(--teal)}
.hero-art{left:28px;top:20px;width:660px;height:532px;background:radial-gradient(ellipse at 50% 60%,#9fe0df 0,var(--teal-soft) 45%,var(--teal) 80%);border-radius:4px}
.hero-copy{left:738px;top:176px;color:var(--white)}
.hero-title{font-size:29px;font-weight:900;line-height:44px;letter-spacing:.2px}
.hero-sub{font-size:27px;font-weight:400;line-height:38px}
.hero-btn{left:740px;top:324px;width:126px;height:37px;font-size:18px}

/* section heading */
.section-title{font-weight:900;font-size:35px;letter-spacing:.3px}
.section-title .accent{color:var(--orange)}

/* why */
.why-title{left:0;top:722px;width:1200px;text-align:center}
.feature{width:260px;text-align:center}
.feature-icon{width:152px;height:152px;border-radius:50%;background:var(--navy);margin:0 auto 22px;display:flex;align-items:center;justify-content:center}
.feature-label{font-size:16px;font-weight:700;line-height:21px;color:var(--ink)}

/* create */
.create{left:0;top:1324px;width:1200px;height:383px;background:var(--orange)}
.devices-art{left:18px;top:63px;width:462px;height:266px;background:linear-gradient(180deg,#f3f3f3,#dcdcdc);border-radius:10px}
.create-title{left:517px;top:36px;color:var(--ink)}
.create-title .accent{color:var(--white)}
.create-text{left:519px;top:93px;width:600px;font-size:14px;line-height:19px;color:var(--ink)}
.create-field{left:519px;top:157px;width:592px;height:131px;background:var(--white);border-radius:2px;font-size:13.5px;color:#555;padding:16px 15px}
.create-btn{left:519px;top:301px;width:105px;height:37px;font-size:18px}

/* quiz */
.quiz{left:0;top:1707px;width:1200px;height:412px;background:var(--steel);color:var(--white)}
.quiz-title{left:73px;top:30px;font-weight:700;font-size:37px}
.quiz-label{left:73px;top:106px;font-size:14px;font-weight:700;color:var(--orange)}
.quiz-question{left:73px;top:129px;width:640px;font-size:14px;line-height:23px}
.quiz-prompt{left:73px;top:188px;font-size:14px;font-weight:700;color:var(--orange)}
.option{font-size:14px;display:flex;align-items:center;gap:9px}
.option-key{width:20px;height:20px;border-radius:50%;background:var(--orange);color:var(--white);font-size:11px;font-weight:700;display:flex;align-items:center;justify-content:center}
.option-key.is-plain{background:var(--white);color:var(--orange)}
.quiz-result{left:73px;top:296px;font-size:14px;font-weight:700;color:var(--orange);display:flex;gap:6px;align-items:center}
.pager{width:37px;height:40px;background:var(--orange);color:var(--white);font-size:22px;font-weight:700}
.pager.is-light{background:var(--white);color:var(--orange)}
.all-btn{left:156px;top:337px;width:176px;height:40px;font-size:18px}
.brain-art{left:755px;top:88px;width:338px;height:285px;background:radial-gradient(ellipse at 60% 45%,#f6b042 0,#d9e2ec 40%,var(--steel) 75%);border-radius:8px}

/* about */
.about-title{left:75px;top:2162px}
.about-text{left:75px;top:2238px;width:560px;font-size:13px;line-height:22px;color:var(--ink)}
.tour-btn{left:75px;top:2400px;width:129px;height:37px;font-size:18px}
.video-art{left:690px;top:2183px;width:462px;height:253px;background:linear-gradient(180deg,#ededed,#cfd2d6);border-radius:8px}

/* footer */
.site-footer{left:0;top:2498px;width:1200px;height:128px;background:var(--steel)}
.footer-dot{width:44px;height:44px;border-radius:50%;background:var(--orange)}
.footer-nav{left:0;top:88px;width:1200px;display:flex;justify-content:center;color:var(--white);font-size:14.5px}
.footer-nav a{padding:0 14px;border-right:1px solid rgba(255,255,255,.4);line-height:16px}
.footer-nav a:last-child{border-right:none}
.copyright{left:0;top:2626px;width:1200px;height:41px;background:var(--steel-dark);color:var(--white);font-size:14.5px;display:flex;align-items:center;justify-content:center}
</style>
</head>
<body>

<header class="site-header abs">
  <div class="brand abs">
    <div class="brand-name">uVeldra</div>
    <div class="brand-tag">The Medical Peer Review</div>
  </div>
  <span class="social-dot abs" style="left:800px;top:18px;background:#3b5998"></span>
  <span class="social-dot abs" style="left:844px;top:18px;background:#dd4b39"></span>
  <span class="social-dot abs" style="left:889px;top:18px;background:#1da1f2"></span>
  <a class="btn btn-orange abs" style="left:944px;top:21px;width:69px;height:31px">Signup</a>
  <a class="btn btn-steel abs" style="left:1038px;top:21px;width:89px;height:31px">Log In</a>
</header>

<nav class="main-nav abs">
  <a class="nav-item is-active">Home</a>
  <a class="nav-item">Take the tour</a>
  <a class="nav-item">Peers say</a>
  <a class="nav-item">Subscription Plans</a>
  <a class="nav-item">Moderation</a>
  <a class="nav-item">Statistics</a>
  <a class="nav-item">Competition</a>
  <a class="nav-item">Answer Ques</a>
  <a class="nav-item">Post Ques</a>
  <a class="nav-item">Friends</a>
  <a class="nav-item">Contact Us</a>
</nav>

<section class="hero abs">
  <div class="hero-art abs" role="img" aria-label="Illustration of two doctors in white coats surrounded by medical icons and a laptop"></div>
  <div class="hero-copy abs">
    <div class="hero-title">BEST LEARNING PLATFORM<br>FOR MEDICAL STUDENTS</div>
    <div class="hero-sub">You Learn with fun &amp; interest</div>
  </div>
  <a class="hero-btn btn btn-orange abs">See Demo</a>
</section>

<section>
  <h2 class="section-title why-title abs">WHY <span class="accent">CHOOSE US</span></h2>
  <svg class="abs" style="left:758px;top:752px" width="120" height="40" viewBox="0 0 120 40"><polyline points="0,22 6,22 11,8 16,34 20,22 120,22" fill="none" stroke="var(--rule)" stroke-width="1.5"/></svg>

  <div class="feature abs" style="left:26px;top:813px">
    <div class="feature-icon"><svg width="80" height="64" viewBox="0 0 80 64"><rect x="12" y="4" width="56" height="40" rx="3" fill="none" stroke="#fff" stroke-width="6"/><rect x="2" y="50" width="76" height="8" rx="3" fill="#fff"/><path d="M40 16l14 8-6 2 4 7-3 2-4-7-5 4z" fill="var(--orange)"/></svg></div>
    <div class="feature-label">Test Your<br>Medical Knowledge</div>
  </div>
  <div class="feature abs" style="left:309px;top:813px">
    <div class="feature-icon"><svg width="60" height="90" viewBox="0 0 60 90"><path d="M8 26a22 22 0 1 1 30 20c-5 2-6 6-6 12v4" fill="none" stroke="#fff" stroke-width="13" stroke-linecap="round"/><circle cx="32" cy="80" r="8" fill="#fff"/></svg></div>
    <div class="feature-label">Answer A Vast Array<br>Of Medical Questions</div>
  </div>
  <div class="feature abs" style="left:617px;top:813px">
    <div class="feature-icon"><svg width="80" height="80" viewBox="0 0 80 80"><path d="M20 6h40v22a20 20 0 0 1-40 0z" fill="#fff"/><path d="M20 12H8c0 14 6 20 14 20M60 12h12c0 14-6 20-14 20" fill="none" stroke="#fff" stroke-width="5"/><rect x="35" y="46" width="10" height="14" fill="#fff"/><rect x="24" y="62" width="32" height="12" fill="var(--orange)"/></svg></div>
    <div class="feature-label">Earn Trophies As &nbsp;Your<br>Knowledge Increases</div>
  </div>
  <div class="feature abs" style="left:917px;top:813px">
    <div class="feature-icon"><svg width="90" height="86" viewBox="0 0 90 86"><path d="M40 4l10 24 26 2-20 17 6 26-22-14-22 14 6-26L4 30l26-2z" fill="#fff"/><path d="M66 40l5 12 13 1-10 8 3 13-11-7-11 7 3-13-10-8 13-1z" fill="var(--orange)"/></svg></div>
    <div class="feature-label">Rate Question<br>From Peers</div>
  </div>

  <div class="feature abs" style="left:26px;top:1058px">
    <div class="feature-icon"><svg width="80" height="80" viewBox="0 0 80 80"><path d="M8 16a10 10 0 1 1 14 9c-3 1-3 3-3 6" fill="none" stroke="#fff" stroke-width="6" stroke-linecap="round"/><circle cx="19" cy="40" r="4" fill="#fff"/><circle cx="46" cy="36" r="10" fill="var(--orange)"/><path d="M30 74V54c0-6 4-8 10-8h12c6 0 10 2 12-6l6-26 6 2-6 30c-2 8-6 10-10 10v18z" fill="var(--orange)"/></svg></div>
    <div class="feature-label">Ask Your Own<br>Questions</div>
  </div>
  <div class="feature abs" style="left:309px;top:1058px">
    <div class="feature-icon"><svg width="90" height="84" viewBox="0 0 90 84"><path d="M45 2a14 14 0 0 1 14 14c0 8-8 12-14 22-6-10-14-14-14-22A14 14 0 0 1 45 2z" fill="var(--orange)"/><text x="45" y="22" text-anchor="middle" font-size="16" font-weight="700" fill="#3f6590" font-family="Lato,sans-serif">?</text><circle cx="45" cy="50" r="8" fill="#fff"/><circle cx="22" cy="56" r="7" fill="#fff"/><circle cx="68" cy="56" r="7" fill="#fff"/><path d="M31 82c0-14 6-20 14-20s14 6 14 20zM8 82c0-12 5-17 14-17 4 0 6 1 8 3M82 82c0-12-5-17-14-17-4 0-6 1-8 3" fill="#fff"/></svg></div>
    <div class="feature-label">Link To Your Friend And<br>Check Their Progress</div>
  </div>
  <div class="feature abs" style="left:617px;top:1058px">
    <div class="feature-icon"><svg width="80" height="80" viewBox="0 0 80 80"><circle cx="40" cy="40" r="34" fill="#fff"/><path d="M16 26c6-6 14-4 16 2s-4 8-2 14-8 8-10 2-8-12-4-18zM44 14c6 0 14 6 12 12s-8 2-10 8 6 10 2 18-10 10-12 4 0-14 0-20-4-12 8-22z" fill="var(--orange)"/></svg></div>
    <div class="feature-label">Create Study Groups<br>Locally Or Internationally</div>
  </div>
  <div class="feature abs" style="left:917px;top:1058px">
    <div class="feature-icon"><svg width="92" height="80" viewBox="0 0 92 80"><rect x="22" y="6" width="64" height="44" rx="8" fill="#fff"/><path d="M70 50l4 12-14-12z" fill="#fff"/><rect x="32" y="16" width="44" height="4" fill="#3f6590"/><rect x="32" y="25" width="44" height="4" fill="#3f6590"/><rect x="32" y="34" width="30" height="4" fill="#3f6590"/><rect x="4" y="40" width="40" height="26" rx="7" fill="var(--orange)"/><path d="M14 66l-4 10 14-10z" fill="var(--orange)"/></svg></div>
    <div class="feature-label">29.903 Question<br>Answered!</div>
  </div>
</section>

<section class="create abs">
  <div class="devices-art abs" role="img" aria-label="Phone and laptop mock-up showing the uVeldra start screen"></div>
  <h2 class="section-title create-title abs">Create <span class="accent">Your Questions</span></h2>
  <svg class="abs" style="left:928px;top:52px" width="140" height="36" viewBox="0 0 140 36"><polyline points="0,22 8,22 13,6 18,32 22,22 140,22" fill="none" stroke="#fff" stroke-width="1.5"/></svg>
  <p class="create-text abs">You Can Create your own questions. Lorem ipsum dolor sit amet, consectetuer adipiscing elit, sed nonummy nibh euismod tincidunt ut laoreet dolore magna aliquam erat volutpat.</p>
  <div class="create-field abs">Create your own question</div>
  <a class="create-btn btn btn-steel abs">Create</a>
</section>

<section class="quiz abs">
  <h2 class="quiz-title abs">Test Your Knowledge</h2>
  <svg class="abs" style="left:462px;top:55px" width="120" height="36" viewBox="0 0 120 36"><polyline points="0,22 6,22 11,6 16,32 20,22 120,22" fill="none" stroke="#a9bdd2" stroke-width="1.5"/></svg>
  <div class="quiz-label abs">Question 1:</div>
  <p class="quiz-question abs">Lorem ipsum dolor sit amet, consectetuer adipiscing elit, sed nonummy nibh tincidunt ut laoreet dolore magna aliquam erat volutpat?</p>
  <div class="quiz-prompt abs">Selcet one option below:</div>
  <div class="option abs" style="left:73px;top:221px"><span class="option-key">A</span><span style="color:#c9d6e4">Lorem ipsum dolor</span></div>
  <div class="option abs" style="left:254px;top:221px"><span class="option-key is-plain">C</span>Lorem ipsum dolor</div>
  <div class="option abs" style="left:73px;top:254px"><span class="option-key is-plain">B</span>Lorem ipsum dolor</div>
  <div class="option abs" style="left:254px;top:254px"><span class="option-key is-plain">D</span>Lorem ipsum dolor</div>
  <div class="quiz-result abs"><svg width="16" height="14" viewBox="0 0 16 14"><path d="M1 7l5 5 9-11" fill="none" stroke="#7bd16b" stroke-width="3"/></svg>CORRECT!</div>
  <a class="pager is-light btn abs" style="left:73px;top:337px">«</a>
  <a class="pager btn abs" style="left:114px;top:337px">»</a>
  <a class="all-btn btn btn-orange abs">See All Questions</a>
  <div class="brain-art abs" role="img" aria-label="Illustration of a brain above a light bulb with gears"></div>
</section>

<section>
  <h2 class="section-title about-title abs">ABOUT <span class="accent">US</span></h2>
  <svg class="abs" style="left:252px;top:2186px" width="90" height="36" viewBox="0 0 90 36"><polyline points="0,22 16,22 21,6 26,32 30,22 90,22" fill="none" stroke="var(--rule)" stroke-width="1.5"/></svg>
  <p class="about-text abs">Lorem ipsum dolor sit amet, consectetuer adipiscing elit, sed diam nonummy nibh euismod tincidunt ut laoreet dolore magna aliquam erat volutpat. Ut wisi enim ad minim veniam, quis nostrud exerci tation ullamcorper suscipit lobortis nisl ut aliquip ex ea commodo consequat. Duis autem vel eum iriure dolor in hendrerit in vulputate velit esse molestie consequat, vel illum dolore eu feugiatulla facilisis at vero eros et accumsan et iusto odio dignissim qui blandit praesent luptatum zzril delenit augue duis dolore te feugait nulla facilisi.</p>
  <a class="tour-btn btn btn-orange abs">Take a Tour</a>
  <div class="video-art abs" role="img" aria-label="Laptop playing an explainer video with a drawn presenter beside a screen"></div>
</section>

<footer>
  <div class="site-footer abs">
    <span class="footer-dot abs" style="left:508px;top:19px"></span>
    <span class="footer-dot abs" style="left:579px;top:19px"></span>
    <span class="footer-dot abs" style="left:646px;top:19px"></span>
    <nav class="footer-nav abs">
      <a>Home</a><a>Take the tour</a><a>What your peers say</a><a>Subscription Plans</a><a>Moderation</a><a>Statistics</a><a>Competition</a><a>Answer Ques</a><a>Post Ques</a><a>Contact Us</a>
    </nav>
  </div>
  <div class="copyright abs">Copyright 2016 uVeldra. All Rights Reserved.</div>
</footer>

</body>
</html>
```